Label for Refill packaging eco-conscious beauty brand

We need a label for our refill pouch. Velvet Harbor is an unscented conditioner formulated using the finest healthy & pure ingredients, free of chemicals and harmful toxins. As a minimalist beauty brand we are proud to be certified with TPL, VerdaSeal and Silver Fawn.

We already have the pouches and an exciting label for our regular bottles.
We choose a kraft brown packing for the refill pouch and would like something minimalist but elegant for the label.

```html
<!DOCTYPE html>
<html lang="en">
<head>
<meta charset="utf-8">
<title>Velvet Harbor – Label Range</title>
<link rel="stylesheet" href="https://fonts.googleapis.com/css2?family=Cormorant+Garamond:ital,wght@0,500;1,500&family=Lato:wght@400&display=swap">
<style>
  :root {
    --stage: #03282f;
    --ink: #ffffff;
    --ink-soft: rgba(255,255,255,0.82);
    --rule: rgba(255,255,255,0.6);
    --sage-light: #b9c9c8;
    --sage-dark: #9fb2b1;
    --stone-light: #e2dfda;
    --stone-dark: #cfcbc4;
    --mauve-light: #977c82;
    --mauve-dark: #7d646a;
  }
  * { margin: 0; padding: 0; box-sizing: border-box; }
  html, body { width: 1200px; height: 837px; overflow: hidden; }
  body {
    background: var(--stage);
    position: relative;
    font-family: "Lato", sans-serif;
    color: var(--ink);
  }
  .label {
    position: absolute;
    top: 322px;
    width: 215px;
    height: 312px;
    overflow: hidden;
  }
  .label--sage  { left: 218px; }
  .label--stone { left: 509px; }
  .label--mauve { left: 823px; top: 326px; }
  .label-texture {
    position: absolute; inset: 0;
  }
  .label--sage .label-texture  { background: linear-gradient(135deg, var(--sage-light), var(--sage-dark)); }
  .label--stone .label-texture { background: linear-gradient(135deg, var(--stone-light), var(--stone-dark)); }
  .label--mauve .label-texture { background: linear-gradient(135deg, var(--mauve-light), var(--mauve-dark)); }
  .label-content {
    position: relative;
    height: 100%;
    display: flex;
    flex-direction: column;
    align-items: center;
    text-align: center;
  }
  .brand {
    margin-top: 40px;
    width: 62px;
    height: 106px;
    display: flex;
    flex-direction: column;
    align-items: center;
    justify-content: flex-end;
    padding-bottom: 10px;
  }
  .brand-square {
    width: 30px; height: 30px;
    border: 1px solid var(--ink);
    margin-bottom: 14px;
  }
  .brand-name {
    font-family: "Lato", sans-serif;
    font-weight: 400;
    font-size: 13px;
    line-height: 1.15;
    color: var(--ink);
  }
  .product-name {
    margin-top: 24px;
    font-family: "Cormorant Garamond", serif;
    font-weight: 500;
    font-size: 16px;
    letter-spacing: 0.02em;
    text-transform: uppercase;
    padding-bottom: 3px;
    border-bottom: 1px solid var(--rule);
    width: 138px;
  }
  .product-desc {
    margin-top: 2px;
    font-size: 8px;
    line-height: 1.15;
    color: var(--ink-soft);
  }
  .certs {
    margin-top: 5px;
    width: 138px;
    padding: 3px 0;
    border-top: 1px solid var(--rule);
    border-bottom: 1px solid var(--rule);
    font-family: "Cormorant Garamond", serif;
    font-style: italic;
    font-size: 7px;
    color: var(--ink-soft);
    display: flex;
    justify-content: center;
    gap: 3px;
  }
  .certs .sep { font-style: normal; }
  .volume {
    margin-top: 40px;
    font-size: 9px;
    color: var(--ink-soft);
  }
</style>
</head>
<body>

  <section class="label label--sage">
    <div class="label-texture" role="img" aria-label="Fine leaf vein texture in sage tones"></div>
    <div class="label-content">
      <div class="brand"><span class="brand-square"></span><span class="brand-name">LUMEN<br>Sorrel</span></div>
      <h2 class="product-name">Velvet Harbor</h2>
      <p class="product-desc">unscented hair conditioner<br>apres - shampoing non parfum</p>
      <p class="certs"><span>TPL Verified</span><span class="sep">|</span><span>VerdaSeal</span><span class="sep">|</span><span>Silver Fawn</span></p>
      <p class="volume">238ml e / 8fl. oz.</p>
    </div>
  </section>

  <section class="label label--stone">
    <div class="label-texture" role="img" aria-label="Fine leaf vein texture in stone tones"></div>
    <div class="label-content">
      <div class="brand"><span class="brand-square"></span><span class="brand-name">LUMEN<br>Sorrel</span></div>
      <h2 class="product-name">Velvet Harbor</h2>
      <p class="product-desc">unscented hair conditioner<br>apres - shampoing non parfum</p>
      <p class="certs"><span>TPL Verified</span><span class="sep">|</span><span>VerdaSeal</span><span class="sep">|</span><span>Silver Fawn</span></p>
      <p class="volume">238ml e / 8fl. oz.</p>
    </div>
  </section>

  <section class="label label--mauve">
    <div class="label-texture" role="img" aria-label="Fine leaf vein texture in mauve tones"></div>
    <div class="label-content">
      <div class="brand"><span class="brand-square"></span><span class="brand-name">LUMEN<br>Sorrel</span></div>
      <h2 class="product-name">Velvet Harbor</h2>
      <p class="product-desc">unscented hair conditioner<br>apres - shampoing non parfum</p>
      <p class="certs"><span>TPL Verified</span><span class="sep">|</span><span>VerdaSeal</span><span class="sep">|</span><span>Silver Fawn</span></p>
      <p class="volume">238ml e / 8fl. oz.</p>
    </div>
  </section>

</body>
</html>
```